Camp Willowbend 2019 Summer Camp Postcard

We are a Christian summer camp offering nine weeks of day camp and two weeks of overnight camp. We need a bright, colorful design that showcases our offered activities such as boating, rock wall, crafts, sports, rock wall. We want our photos highlighted/enhanced. Our colors are red, orange, brown and black.

Target Market(s)

Parents of elementary age children

Industry/Entity Type

Christian

Font styles to use
Sans Serif

Colors
fbee3d
fece3e
ffc214
ec1f27
f04a50
f37122
f78f20
333333
faa54b

Requirements
Must have
• Must Have:
• Day Camp 2019
• June 24 - August 23
• $135 per week
• Mon-Fri 8 am to 4 pm. Open to kids entering grades 1 to 8. Day camp is chock full of activities like swimming, rock wall, archery, sports, crafts, air rifles and much more! Daily lunch and snack included. Before and after-care available at an extra rate.
• Register and pay in full by April 1st, save $270!
• Overnight Camp 2018
• July 14-20 and July 21-27
• $330 per week
• Open to kids ages 8 to 14. Spend the week making new friends, sleeping in cabins, climbing the rock wall and swimming at the beach! Our guest speakers will lead twice daily chapel sessions that will challenge campers to grow in their faith.
• 42 Marsh Creek Rd. Alder Falls, ME 04917
• 603-555-0148
• www.willowbendcamp-example.org
Nice to have
• Bright and colorful
• Photos of happy campers participating in our listed activities

```html
<!DOCTYPE html>
<html lang="en">
<head>
<meta charset="utf-8">
<title>Camp Willowbend – Postcard Back</title>
<link rel="stylesheet" href="https://fonts.googleapis.com/css2?family=Arvo&family=Lato:wght@400;700;900&display=swap">
<style>
  :root {
    --page: #ffffff;
    --ink: #111111;
    --wood-light: #d9b27a;
    --wood-mid: #c2925a;
    --panel: #5b3414;
    --heading: #f7941d;
    --body: #ffffff;
    --brand-red: #c8202a;
  }
  * { margin: 0; padding: 0; box-sizing: border-box; }
  html, body { width: 1200px; height: 1200px; overflow: hidden; background: var(--page); }
  .canvas { position: relative; width: 1200px; height: 1200px; }

  .side-label {
    position: absolute; left: 59px; top: 150px;
    font: 900 25px/1 "Lato", sans-serif; color: var(--ink);
  }

  .postcard {
    position: absolute; left: 105px; top: 253px; width: 994px; height: 684px;
    overflow: hidden;
  }
  .wood-photo {
    position: absolute; inset: 0;
    background: linear-gradient(180deg, var(--wood-light) 0%, var(--wood-mid) 45%, var(--wood-light) 70%, var(--wood-mid) 100%);
  }
  .campfire-art {
    position: absolute; right: 0; top: 0; width: 200px; height: 150px;
    background: rgba(255,255,255,0.18);
  }
  .paddle-art {
    position: absolute; left: 0; bottom: 0; width: 310px; height: 110px;
    background: rgba(255,255,255,0.2);
  }

  .info-panel {
    position: absolute; left: 66px; top: 36px; width: 886px; height: 534px;
    background: var(--panel);
    padding: 16px 10px 0 18px;
  }
  .camp-heading {
    font: 400 27.5px/35px "Arvo", serif; color: var(--heading);
    padding-left: 5px; white-space: nowrap;
  }
  .camp-copy {
    font: 400 27px/35px "Lato", sans-serif; color: var(--body);
    padding-left: 2px; white-space: nowrap;
  }
  .camp-copy.overnight { padding-left: 6px; }
  .overnight-heading { margin-top: 3px; padding-left: 0; }
  .contact {
    font: 400 27px/34px "Arvo", serif; color: var(--heading);
    font-style: normal; margin-top: 12px; white-space: nowrap;
  }
  .contact .web { margin-left: 34px; }

  .brand {
    position: absolute; right: 66px; bottom: 22px;
    display: flex; align-items: center; gap: 10px;
  }
  .brand-dot { width: 30px; height: 30px; border-radius: 50%; background: var(--brand-red); }
  .brand-name { font: 900 30px/1 "Lato", sans-serif; color: var(--brand-red); }
</style>
</head>
<body>
<div class="canvas">
  <div class="side-label">BACK</div>

  <section class="postcard">
    <div class="wood-photo" role="img" aria-label="Photo of light wooden planks"></div>
    <div class="campfire-art" role="img" aria-label="Line illustration of a small campfire with crossed logs"></div>
    <div class="paddle-art" role="img" aria-label="White illustration of a canoe paddle"></div>

    <div class="info-panel">
      <div class="day-camp">
        <h2 class="camp-heading">DAY CAMP 2019&nbsp; JUNE 24-AUGUST 23&nbsp; $135 per week</h2>
        <h2 class="camp-heading">MON-FRI 8am to 4pm</h2>
        <p class="camp-copy">Open to kids entering grades 1 tp 8.&nbsp; Day Camp is<br>
        chock full of activities like swimming, rock wall, archery, sports<br>
        crafts, air rifles and much more!&nbsp; Daily lunch and snack included.<br>
        Before and after care available at an extra rate.<br>
        Register and pay in full by April 1st, save $270!</p>
      </div>
      <div class="overnight-camp">
        <h2 class="camp-heading overnight-heading">OVERNIGHT&nbsp; CAMP 2018&nbsp; JULY14-20&nbsp; -JULY 21-27&nbsp; $330 per week</h2>
        <p class="camp-copy overnight">Open to kids ages 8 to 14.&nbsp; Spend the week making new friends,<br>
        sleeping in cabins, climbing the rock wall and swimming at the beach!<br>
        Our guest speakers will lead twice daily chapel sessions that will<br>
        challenge campers to grow in their faith.</p>
      </div>
      <address class="contact">
        42 Marsh Creek Rd. Alder Falls, ME 04917<br>
        603-555-0148<span class="web">www.willowbendcamp-example.org</span>
      </address>
    </div>

    <div class="brand">
      <span class="brand-dot"></span>
      <span class="brand-name">Camp Willowbend</span>
    </div>
  </section>
</div>
</body>
</html>
```